Brochure Design Project

We need a brochure design, copy writing and print ready art for a Toronto based commercial cleaning company. Output should be an 8.5X11 four page piece.

We provide "green cleaning" - environmentally friendly cleaning programs. Our positioning is strongly environmentally oriented, high quality, reliable and affordable.

We provide interior cleaning for office buildings, condominiums, manufacturing facilities, gyms, retail stores, daycares, churches and banquet facilities.

Core services are; regularly scheduled cleaning programs, floor maintenance, carpet cleaning, window cleaning, construction cleaning and sanitary supply management.

Looking for a "fresh" clean look that screams "competent" and "professional" and clearly communicates "affordability"

The piece will be used as a stand alone mailer and leave behind for a salesperson.

Reason: Designs have not met the brief specifications

Target Market(s)

Mid level managers of virtually every "non food service" company, facility or operation. Slightly skewed to female decision makers

Industry/Entity Type

Construction

Requirements
Must have
• Clear identification of the key services with image support, ie floor maintenance image, carpet cleaning

```html
<!DOCTYPE html>
<html lang="en">
<head>
<meta charset="utf-8">
<title>Fresh Sweep – Green Cleaning Brochure</title>
<link href="https://fonts.googleapis.com/css2?family=Open+Sans:wght@400;600;700&display=swap" rel="stylesheet">
<style>
  :root {
    --band-green: #8cbf3f;
    --ink-green: #1e5a2c;
    --text-green: #2a5a30;
    --bullet-green: #8cbf3f;
    --price-box: #c6dd92;
    --price-head: #9cc653;
    --photo-sky: #dfe9d8;
    --photo-leaf: #7aa14a;
    --paper: #ffffff;
    --tile-light: #e6f0d4;
    --tile-deep: #6f9a3a;
  }
  * { box-sizing: border-box; margin: 0; padding: 0; }
  html, body { width: 1200px; height: 848px; overflow: hidden; background: var(--paper); }
  body { font-family: "Open Sans", Arial, sans-serif; color: var(--text-green); position: relative; }

  .band { position: absolute; left: 0; width: 1200px; background: var(--band-green); }
  .band--top { top: 0; height: 74px; }
  .band--bottom { top: 774px; height: 74px; }

  .services { list-style: none; display: flex; justify-content: space-between; padding: 0 20px; height: 74px; align-items: center; }
  .service { display: flex; align-items: center; gap: 10px; width: 186px; }
  .service__image { flex: none; width: 50px; height: 50px; border: 2px solid var(--paper); }
  .service__name { font-size: 14px; font-weight: 700; line-height: 17px; color: var(--paper); }

  .panel { position: absolute; top: 88px; }
  .panel--left { left: 20px; width: 370px; }
  .panel--middle { left: 410px; width: 378px; }
  .panel--right { left: 810px; width: 370px; top: 84px; }

  .intro p { font-size: 17.5px; line-height: 22.5px; color: var(--ink-green); margin-bottom: 22px; }
  .intro p:last-child { margin-bottom: 0; }

  h2 { font-size: 21.5px; font-weight: 700; color: var(--ink-green); line-height: 26px; }
  .body-text { font-size: 15.2px; line-height: 20px; text-align: justify; color: var(--text-green); hyphens: auto; }
  .body-text + .body-text { margin-top: 7px; }

  .green-program h2 { margin: 24px 0 3px; }
  .benefits-title { font-size: 14.6px; font-weight: 700; color: var(--ink-green); line-height: 20px; margin: 16px 0 12px; }

  .benefit-list { list-style: none; }
  .benefit-list li { position: relative; padding-left: 17px; font-size: 14.6px; line-height: 20px; margin-bottom: 5px; }
  .benefit-list li::before { content: ""; position: absolute; left: 1px; top: 7px; width: 7px; height: 7px; background: var(--bullet-green); }
  .benefit-list li.plain { margin-top: -3px; }
  .benefit-list li.plain::before { display: none; }
  .benefit-list li.mark-high::before { top: 1px; }
  .panel--middle .benefit-list li { margin-bottom: 5.5px; }

  .scope { margin-top: 28px; }

  .pricing { position: absolute; left: 409px; top: 564px; width: 379px; height: 196px; background: var(--price-box); }
  .pricing__head { background: var(--price-head); height: 64px; padding: 6px 19px; }
  .pricing__head h2 { font-size: 20.5px; line-height: 26px; }
  .pricing__sub { font-size: 14.6px; font-weight: 700; color: var(--ink-green); line-height: 22px; margin-top: 2px; }
  .price-table { margin: 14px 19px 0; border-collapse: collapse; font-size: 14.6px; color: var(--text-green); }
  .price-table td { line-height: 20px; vertical-align: top; padding: 0; }
  .price-table td:first-child { width: 212px; }

  .photo { display: block; width: 390px; height: 214px; }

  .guarantee h2 { margin: 6px 0 3px; }
  .guarantee .body-text + .body-text { margin-top: 20px; }
  .keen h2 { margin: 20px 0 4px; }
</style>
</head>
<body>
  <div class="band band--top"></div>

  <section class="panel panel--left">
    <div class="intro">
      <p>Powered by over 25 years of<br>facilities management experience.</p>
      <p>Built on a foundation of integrity<br>and reliability with a quality service ethic.</p>
      <p>Charged with passion for excellence<br>and desire to improve our way of life.</p>
      <p>Fresh Sweep will deliver a professional, environmentally friendly, effective, efficient and affordable maintenance program .</p>
    </div>
    <div class="green-program">
      <h2>Green Cleaning Program</h2>
      <p class="body-text">Green cleaning refers to using cleaning methods and products with environmentally-friendly ingredients to preserve human health and environmental quality.</p>
      <p class="body-text">Green cleaning techniques and products avoid the use of chemically-reactive and toxic cleaning products which contain various toxic chemicals, some of which emit volatile organic compounds causing respiratory and dermatological problems among other adverse effects</p>
      <p class="benefits-title">Many benefits are associated<br>with a green cleaning program including:</p>
      <ul class="benefit-list">
        <li>Improved indoor air quality.</li>
        <li>Fewer complaints from staff about their indoor environment.</li>
      </ul>
    </div>
  </section>

  <section class="panel panel--middle">
    <ul class="benefit-list">
      <li>Reduced or no adverse environmental impact.</li>
      <li>Saving company owners money.</li>
      <li>Conserving natural resources.</li>
      <li>Enhancing and protecting natural habitats.</li>
      <li class="plain">Improving employee productivity and satisfaction.</li>
      <li class="mark-high">Optimizing life-cycle performance of building materials.</li>
      <li class="plain">Contributing to the health and well-being of the community.</li>
    </ul>
    <div class="scope">
      <p class="body-text">Fresh Sweep will furnish all labor, supervision, cleaning products and equipment, excluding customer consumed sanitary products and supplies, to provide a thorough green cleaning program and maintain the areas outlined in the cleaning specification.</p>
      <p class="body-text">All work will be professionally performed with quality workmanship at the specific times and frequency to be determined with Corner Pharmacy Co.</p>
    </div>
  </section>

  <section class="pricing">
    <div class="pricing__head">
      <h2>Pricing</h2>
      <p class="pricing__sub">Monthly Maintenance (MM)</p>
    </div>
    <table class="price-table">
      <tr><td>2X per week cycle</td><td>$&nbsp;&nbsp;897&nbsp; per month</td></tr>
      <tr><td>3X per week cycle</td><td>$ 1334&nbsp; per month</td></tr>
      <tr><td>Semi Annual Maintenance<br>(SAM)</td><td>$ 1940&nbsp; per event</td></tr>
    </table>
  </section>

  <section class="panel panel--right">
    <svg class="photo" role="img" aria-label="Photo of a cleaner wiping a glass window outdoors with a garden and patio umbrella behind" viewBox="0 0 390 214" preserveAspectRatio="none">
      <defs>
        <linearGradient id="photoTone" x1="0" y1="0" x2="1" y2="1">
          <stop offset="0" stop-color="#dfe9d8"/>
          <stop offset="0.55" stop-color="#a9c27f"/>
          <stop offset="1" stop-color="#7aa14a"/>
        </linearGradient>
      </defs>
      <rect width="390" height="214" fill="url(#photoTone)"/>
    </svg>
    <div class="guarantee">
      <h2>Our Guarantee</h2>
      <p class="body-text">We commit to 100% satisfaction. Should any of our cleaning tasks fall short of your expectations, we will promptly return and repeat the task until you are completely satisfied. Our goal is to provide the best service available.</p>
      <p class="body-text">Professionalism and reliability you can count on. Our cleaners have been carefully selected and properly trained to understand and deliver high quality green cleaning programs.&nbsp; Before joining Fresh Sweep our staff have submitted to background checks to help ensure the integrity of our service. In addition we conduct monthly inspections to ensure the quality of our program.</p>
    </div>
    <div class="keen">
      <h2>Keen to Clean</h2>
      <p class="body-text">We can finalize your custom specifications, train staff, put equipment and supplies in place to start your program within 2 weeks of receiving your approval.</p>
    </div>
  </section>

  <footer class="band band--bottom">
    <svg width="0" height="0" style="position:absolute" aria-hidden="true">
      <defs>
        <linearGradient id="tileTone" x1="0" y1="0" x2="1" y2="1">
          <stop offset="0" stop-color="#e6f0d4"/>
          <stop offset="1" stop-color="#6f9a3a"/>
        </linearGradient>
      </defs>
    </svg>
    <ul class="services">
      <li class="service">
        <svg class="service__image" role="img" aria-label="Photo of an office being cleaned on a regular schedule" viewBox="0 0 50 50"><rect width="50" height="50" fill="url(#tileTone)"/></svg>
        <span class="service__name">Scheduled<br>Cleaning</span>
      </li>
      <li class="service">
        <svg class="service__image" role="img" aria-label="Photo of a floor machine polishing a hard floor" viewBox="0 0 50 50"><rect width="50" height="50" fill="url(#tileTone)"/></svg>
        <span class="service__name">Floor<br>Maintenance</span>
      </li>
      <li class="service">
        <svg class="service__image" role="img" aria-label="Photo of a carpet being deep cleaned with an extractor" viewBox="0 0 50 50"><rect width="50" height="50" fill="url(#tileTone)"/></svg>
        <span class="service__name">Carpet<br>Cleaning</span>
      </li>
      <li class="service">
        <svg class="service__image" role="img" aria-label="Photo of a squeegee clearing a window pane" viewBox="0 0 50 50"><rect width="50" height="50" fill="url(#tileTone)"/></svg>
        <span class="service__name">Window<br>Cleaning</span>
      </li>
      <li class="service">
        <svg class="service__image" role="img" aria-label="Photo of a newly built interior being cleaned after construction" viewBox="0 0 50 50"><rect width="50" height="50" fill="url(#tileTone)"/></svg>
        <span class="service__name">Construction<br>Cleaning</span>
      </li>
      <li class="service">
        <svg class="service__image" role="img" aria-label="Photo of stocked washroom supplies on a shelf" viewBox="0 0 50 50"><rect width="50" height="50" fill="url(#tileTone)"/></svg>
        <span class="service__name">Sanitary Supply<br>Management</span>
      </li>
    </ul>
  </footer>
</body>
</html>
```